business card for WRT pty ltd

We require a business card that stands out . I have included our company flyer and would like the services listed to be put on the card so when we Give out the cards to customers they have an idea of services we provide. need the winning design to be in editable photo shop format, editable iMac pages format or editable windows publisher format, so that I can enter in names, email addresses, phone numbers etc myself. I have included a pdf documents of info / items needed on the card to use as reference please.
Updates

need more submissions

Need extra days to review

Sick

Target Market(s)

new customers

Contact Information for Business Card

details are on attached business card requirements file

Requirements
Must have
• I have attached a list of must haves

```html
<!DOCTYPE html>
<html lang="en">
<head>
<meta charset="utf-8">
<title>WRT pty ltd – Business Card</title>
<link href="https://fonts.googleapis.com/css2?family=Montserrat:wght@400;600;700&display=swap" rel="stylesheet">
<style>
  :root {
    --page: #e4e4e4;
    --card: #0c0c0c;
    --card-soft: #1c1c1c;
    --gold: #b98a3f;
    --gold-text: #c08f45;
    --white: #ffffff;
    --earth: #b0693a;
    --sky: #7fa7d6;
  }
  * { margin: 0; padding: 0; box-sizing: border-box; }
  html, body { width: 1200px; height: 960px; overflow: hidden; }
  body {
    background: var(--page);
    font-family: "Montserrat", sans-serif;
    color: var(--white);
    position: relative;
  }
  .card {
    position: absolute;
    left: 320px;
    width: 570px;
    height: 349px;
    overflow: hidden;
    background: radial-gradient(ellipse at 30% 20%, var(--card-soft), var(--card) 70%);
  }
  .card--front { top: 109px; }
  .card--back { top: 500px; }

  /* front */
  .brand-name {
    position: absolute;
    left: 34px; top: 82px;
    font-size: 74px; font-weight: 700;
    letter-spacing: 2px;
    color: #9a9a9a;
    line-height: 1;
  }
  .front-photo {
    position: absolute;
    left: 0; bottom: 0;
    width: 570px; height: 160px;
    background: linear-gradient(to bottom, rgba(12,12,12,0) 0%, #3a2d22 35%, #9a5e35 70%, var(--earth) 100%);
  }
  .contact { position: absolute; left: 308px; top: 44px; width: 240px; }
  .contact__name { font-size: 19px; font-weight: 700; color: var(--gold-text); }
  .contact__role { font-size: 14px; margin-top: 1px; }
  .contact__company { font-size: 15px; font-weight: 700; margin-top: 17px; }
  .contact__address { font-size: 14px; line-height: 19px; margin-top: 1px; }
  .contact__line { display: flex; align-items: center; gap: 6px; font-size: 14px; white-space: nowrap; }
  .contact__line--phone { font-size: 15px; margin-top: 6px; }
  .contact__line--email { margin-top: 2px; }
  .contact__line svg { width: 13px; height: 13px; flex: none; }
  .web-band {
    position: absolute; right: 0; bottom: 0;
    width: 265px; height: 30px;
    background: var(--gold);
    clip-path: polygon(30px 0, 100% 0, 100% 100%, 0 100%);
    font-size: 14px; font-weight: 700;
    text-align: right; padding-right: 30px; line-height: 30px;
  }

  /* back */
  .back-photo {
    position: absolute; left: 0; top: 0;
    width: 250px; height: 349px;
    clip-path: polygon(0 0, 65px 0, 245px 100%, 0 100%);
    background: linear-gradient(to bottom, var(--sky) 0%, #c9d3de 35%, #dcdcdc 55%, #6d6d6d 80%, #4a4a4a 100%);
  }
  .brand-ghost {
    position: absolute; left: 212px; top: 86px;
    font-size: 100px; font-weight: 700;
    color: rgba(255,255,255,0.06);
    line-height: 1;
  }
  .services { position: absolute; top: 35px; left: 0; list-style: none; }
  .services li {
    position: relative;
    font-size: 15px; font-weight: 700;
    line-height: 19px; white-space: nowrap;
  }
  .services li::before {
    content: "";
    position: absolute; left: -13px; top: 8px;
    width: 4px; height: 4px; border-radius: 50%;
    background: var(--gold);
  }
  .services li.services__cont::before { display: none; }
  .offer-band {
    position: absolute; right: 0; top: 284px;
    width: 453px; height: 42px;
    background: var(--gold);
    clip-path: polygon(22px 0, 100% 0, 100% 100%, 0 100%);
    text-align: right; padding-right: 18px;
    font-size: 14px; line-height: 18px; padding-top: 3px;
  }
</style>
</head>
<body>
  <section class="card card--front">
    <div class="front-photo" role="img" aria-label="Photo of a road train with tipper trailers on red outback dirt"></div>
    <div class="brand-name">WRT</div>
    <div class="contact">
      <p class="contact__name">Daniel Hartley</p>
      <p class="contact__role">Director</p>
      <p class="contact__company">WRT pty ltd</p>
      <p class="contact__address">Depot: Lot 12 sample road<br>Australia</p>
      <p class="contact__line contact__line--phone">
        <svg viewBox="0 0 24 24"><path fill="var(--gold)" d="M6.6 10.8a15.1 15.1 0 0 0 6.6 6.6l2.2-2.2c.3-.3.7-.4 1-.2 1.1.4 2.3.6 3.6.6.6 0 1 .4 1 1V20c0 .6-.4 1-1 1A17 17 0 0 1 3 4c0-.6.4-1 1-1h3.5c.6 0 1 .4 1 1 0 1.3.2 2.5.6 3.6.1.3 0 .7-.2 1z"/></svg>
        000 555 000
      </p>
      <p class="contact__line contact__line--email">
        <svg viewBox="0 0 24 24"><rect x="2" y="5" width="20" height="14" fill="none" stroke="var(--gold)" stroke-width="2.4"/><path d="M2 5l10 8 10-8" fill="none" stroke="var(--gold)" stroke-width="2.4"/></svg>
        email@wrtransport.com.au
      </p>
    </div>
    <div class="web-band">www.websiteaddress.com</div>
  </section>

  <section class="card card--back">
    <div class="back-photo" role="img" aria-label="Photo of a white prime mover road train tanker under blue sky"></div>
    <div class="brand-ghost">WRT</div>
    <ul class="services">
      <li style="left:221px">Over Size Loads / Hot Shot Loads</li>
      <li style="left:231px">Heavy Vehicle Recovery Services</li>
      <li style="left:241px">Potable Water Deliveries</li>
      <li style="left:251px">Road Building / Maintenance</li>
      <li style="left:261px">Earthworks</li>
      <li style="left:271px">Sand &amp; Metal Supply &amp; Cartage</li>
      <li style="left:281px">Road Train Tippers</li>
      <li style="left:291px">Road Train Tankers</li>
      <li style="left:301px">Road Train Flat Tops</li>
      <li style="left:311px">Drop Deck Trailers</li>
      <li style="left:321px">Mine Site Accredited</li>
      <li class="services__cont" style="left:331px">Equipment &amp; Operators</li>
    </ul>
    <div class="offer-band">We offer a large range of services not listed.<br>so call us today for a personalised quote to suit your needs.</div>
  </section>
</body>
</html>
```